Silver Brook Custom Homes business card. Double sided. Modern. professional

Silver Brook Custom Homes
contemporary modern design with our logo /
Double sided with all our contact information
Use same Green colors as in our Logo. Contemporary logo that grabs your attention. Visually pleasing and balanced. Easy to read, and Vibrant. Would love an option for rounded edges. Embossed logo would be amazing.
Contact Information for Business Card
Dana Pellman Owner / General Contractor Silver Brook Custom Homes p: 803.555.0142 m: 865.555.0178 e: silverbrookcustomhomes@mailnest.example w: www.silverbrookcustomhomes.example 218 Wrenfield Mill Road Brindlewood, NC 29088

```html
<!DOCTYPE html>
<html lang="en">
<head>
<meta charset="utf-8">
<title>Silver Brook Custom Homes – Business Card</title>
<link rel="stylesheet" href="https://fonts.googleapis.com/css2?family=Roboto:wght@400;700&display=swap">
<style>
  :root {
    --bg: #8a8a88;
    --card-white: #ffffff;
    --brand-green: #5e7233;
    --name-green: #4f6a1e;
    --title-green: #6c8a2a;
    --text-gray: #3f3f3f;
    --rule-green: #7a8f3e;
  }
  * { box-sizing: border-box; margin: 0; padding: 0; }
  html, body {
    width: 1200px; height: 801px; overflow: hidden;
    background: var(--bg);
    font-family: "Roboto", Arial, sans-serif;
  }
  .stage { position: relative; width: 1200px; height: 801px; }
  .card {
    position: absolute; top: 246px;
    width: 540px; height: 309px;
    border-radius: 6px;
    box-shadow: 0 6px 18px rgba(0,0,0,.25);
    overflow: hidden;
  }
  .card-front { left: 40px; background: var(--card-white); border-bottom: 3px solid var(--brand-green); }
  .card-back { left: 620px; background: var(--brand-green); }

  .front-brand {
    position: absolute; left: 36px; top: 50px; width: 240px;
    display: flex; align-items: center; gap: 10px;
  }
  .brand-mark {
    flex: none; width: 22px; height: 22px; border-radius: 50%;
    background: var(--brand-green);
  }
  .brand-name {
    font-size: 20px; font-weight: 400; line-height: 1.2;
    color: var(--brand-green); letter-spacing: .5px;
  }

  .person { position: absolute; right: 26px; top: 104px; text-align: right; }
  .person-name {
    font-size: 21px; font-weight: 700; color: var(--name-green);
    letter-spacing: -.2px; text-transform: uppercase; line-height: 1.2;
  }
  .person-title { font-size: 13px; color: var(--title-green); margin-top: 2px; }

  .divider {
    position: absolute; left: 96px; right: 26px; top: 166px;
    height: 1px; background: var(--rule-green);
  }

  .address {
    position: absolute; right: 26px; top: 178px; text-align: right;
    font-size: 13px; font-style: normal; color: var(--text-gray); line-height: 1.4;
  }

  .contacts-rule {
    position: absolute; left: 36px; width: 120px; top: 212px;
    height: 1px; background: var(--rule-green);
  }
  .contacts {
    position: absolute; left: 36px; top: 220px; list-style: none;
    font-size: 13px; color: var(--text-gray); line-height: 1.4;
  }
  .contacts li { display: flex; align-items: center; gap: 7px; }
  .contacts svg { width: 11px; height: 11px; fill: var(--brand-green); flex: none; }

  .back-brand {
    position: absolute; inset: 0;
    display: flex; flex-direction: column; align-items: center; justify-content: center; gap: 14px;
  }
  .back-brand .brand-mark { width: 40px; height: 40px; background: var(--card-white); }
  .back-brand .brand-name { color: var(--card-white); font-size: 26px; }
</style>
</head>
<body>
<main class="stage">
  <section class="card card-front" aria-label="Business card front">
    <div class="front-brand">
      <span class="brand-mark"></span>
      <span class="brand-name">Silver Brook Custom Homes</span>
    </div>

    <div class="person">
      <p class="person-name">Dana Pellman</p>
      <p class="person-title">Owner / General Contractor</p>
    </div>

    <div class="divider"></div>

    <address class="address">
      218 Wrenfield Mill Road<br>
      Brindlewood, NC 29088
    </address>

    <div class="contacts-rule"></div>
    <ul class="contacts">
      <li><svg viewBox="0 0 12 12"><path d="M3 1l2 2-1 1.5c.7 1.4 1.8 2.5 3.5 3.5L9 7l2 2-1.5 2C5 10.5 1.5 7 1 2.5z"/></svg>803.555.0142</li>
      <li><svg viewBox="0 0 12 12"><path d="M3.5 0h5a1 1 0 011 1v10a1 1 0 01-1 1h-5a1 1 0 01-1-1V1a1 1 0 011-1zm.5 1.5v8h4v-8z"/></svg>865.555.0178</li>
      <li><svg viewBox="0 0 12 12"><path d="M0 2h12v8H0zm1 1l5 3.5L11 3z"/></svg>silverbrookcustomhomes@mailnest.example</li>
      <li><svg viewBox="0 0 12 12"><circle cx="6" cy="6" r="5.5"/></svg>www.silverbrookcustomhomes.example</li>
    </ul>
  </section>

  <section class="card card-back" aria-label="Business card back">
    <div class="back-brand">
      <span class="brand-mark"></span>
      <span class="brand-name">Silver Brook Custom Homes</span>
    </div>
  </section>
</main>
</body>
</html>
```